Tarjetas de visita para empresa de aluminio

Empresa con mas de 40 años vendiendo perfiles de aluminio.
Somos fábrica y almacén, queremos renovar la tarjeta de presentación de nuestros comerciales dando una imgen innovadora y tecnógica mezclado con la calidez del respeto al medio ambiente.
Añado el logo de la empresa y actual cara trasera de la tarjeta de visita, el logo es el simbolo WM y la marca TRAVENIC EXTRUSION, la frase 2extrusion y lacado de aluminio" debe cambiarse por "Diseño, extrusión, lacado, anodizado y mecanizado de precisión de aluminio" o en su defecto incluir todos esos servicios que hacemos o una frase mas pegadiza.

We are an aluminium factory, we produce and stock profiles of aluminium.
we want to renew visit card of our sellers, we are looking for something that show innovation, tecnology and environment respect.
Upload our actual logo and back of visit card, logo WM and brand TRAVENIC EXTRUSION must be keept.
Text "Extrusion y lacado de aluminio" must be changed for "Diseño, extrusion, lacado, anodizado y mecanizado de precisión de aluminio" or something like that

```html
<!DOCTYPE html>
<html lang="es">
<head>
<meta charset="utf-8">
<title>Tarjetas de visita — Travenic Extrusion</title>
<link rel="stylesheet" href="https://fonts.googleapis.com/css2?family=Cinzel:wght@600;700&family=Michroma&display=swap">
<style>
  :root {
    --navy: #06537b;
    --sky: #0381c8;
    --white: #ffffff;
    --silver: #e4e6e8;
    --edge: #1d2a33;
  }
  html, body {
    margin: 0;
    width: 1200px;
    height: 1200px;
    overflow: hidden;
    background: var(--white);
  }
  .sheet { display: block; width: 1200px; height: 1200px; }
  .card-fill { fill: var(--navy); }
  .card-edge { fill: none; stroke: var(--edge); stroke-width: 1; }
  .wave-light { fill: var(--sky); }
  .tech { font-family: "Michroma", sans-serif; }
  .serif { font-family: "Cinzel", serif; font-weight: 700; }
  .brand-symbol { fill: var(--silver); }
  .brand-name { fill: var(--silver); }
  .tagline { fill: var(--white); }
  .contact { fill: var(--white); font-weight: 600; }
  .person-name { fill: var(--navy); }
  .person-rule { stroke: var(--navy); stroke-width: 2; }
  .role { fill: var(--navy); }
  .address { fill: var(--navy); font-weight: 600; }
  .web { fill: var(--white); font-weight: 600; }
</style>
</head>
<body>
<svg class="sheet" viewBox="0 0 1200 1200" xmlns="http://www.w3.org/2000/svg">

  <!-- Front of card -->
  <g class="card card-front">
    <rect class="card-fill" x="140" y="69" width="937" height="507"/>
    <rect class="card-edge" x="140" y="69" width="937" height="507"/>

    <text class="tech brand-symbol" x="608" y="292" font-size="104" text-anchor="middle">WM</text>

    <text class="tech brand-name" x="258" y="435" font-size="50" textLength="702" lengthAdjust="spacingAndGlyphs">TRAVENIC EXTRUSION</text>

    <g class="tech tagline" font-size="22">
      <text x="297" y="474" textLength="608" lengthAdjust="spacingAndGlyphs">DISEÑO, EXTRUSION, LACADO,</text>
      <text x="318" y="504" textLength="565" lengthAdjust="spacingAndGlyphs">ANODIZADO Y MECANIZADO</text>
      <text x="315" y="535" textLength="570" lengthAdjust="spacingAndGlyphs">DE PRECISIÓN DE ALUMINIO</text>
    </g>
  </g>

  <!-- Back of card -->
  <g class="card card-back">
    <rect x="138" y="609" width="940" height="511" fill="var(--white)"/>
    <path class="card-fill" d="M138,609 H1078 V700 L583,773 C470,820 360,860 290,848 C220,840 170,825 138,808 Z"/>
    <path class="wave-light" d="M583,773 C700,720 820,650 930,635 C990,627 1040,640 1078,652 V800 C1020,840 960,855 900,853 C800,850 700,815 583,773 Z"/>
    <rect class="card-fill" x="138" y="1070" width="940" height="50"/>
    <rect class="card-edge" x="138" y="609" width="940" height="511"/>

    <text class="tech brand-symbol" x="336" y="695" font-size="44" text-anchor="middle">WM</text>
    <text class="tech brand-name" x="191" y="753" font-size="21" textLength="290" lengthAdjust="spacingAndGlyphs">TRAVENIC EXTRUSION</text>
    <g class="tech tagline" font-size="10">
      <text x="211" y="771" textLength="250" lengthAdjust="spacingAndGlyphs">DISEÑO, EXTRUSION, LACADO,</text>
      <text x="220" y="784" textLength="232" lengthAdjust="spacingAndGlyphs">ANODIZADO Y MECANIZADO</text>
      <text x="218" y="797" textLength="236" lengthAdjust="spacingAndGlyphs">DE PRECISIÓN DE ALUMINIO</text>
    </g>

    <g class="serif contact" font-size="30">
      <text y="733"><tspan x="734">MÓVIL:</tspan><tspan x="857">600 12 34 56</tspan></text>
      <text y="765"><tspan x="734">TELF</tspan><tspan x="843">: 955 00 11 22</tspan></text>
      <text y="797"><tspan x="732">FAX</tspan><tspan x="841">: 955 00 11 23</tspan></text>
    </g>

    <text class="serif person-name" x="600" y="925" font-size="46" text-anchor="middle" textLength="569" lengthAdjust="spacingAndGlyphs">MARCOS LORENTE RÍOS</text>
    <line class="person-rule" x1="327" y1="939" x2="873" y2="939"/>
    <text class="serif role" x="446" y="969" font-size="24" textLength="296" lengthAdjust="spacing">COMERCIAL</text>

    <g class="serif address" font-size="20">
      <text x="211" y="1024" textLength="778" lengthAdjust="spacingAndGlyphs">POL. IND. EL OLIVAR - C/4 Nº 22,  41900 VILLASERENA (SEVILLA)</text>
      <text x="214" y="1053" textLength="772" lengthAdjust="spacingAndGlyphs">APARTADO DE CORREOS 245   E-MAIL: MARCOSLORENTE@TRAVENIC.COM</text>
    </g>

    <text class="serif web" x="451" y="1103" font-size="20" textLength="294" lengthAdjust="spacing">WWW.TRAVENIC.COM</text>
  </g>
</svg>
</body>
</html>
```